New design of old website

We need a new design of our domain name reseller website.

quilanorte.com

we would also like new design for Logo and all.

the site will be in English and portuguesse,

Industry/Entity Type

Domain

```html
<!DOCTYPE html>
<html lang="en">
<head>
<meta charset="utf-8">
<title>Quilanorte — Domain Reseller</title>
<link rel="stylesheet" href="https://fonts.googleapis.com/css2?family=Ubuntu:wght@400;500&family=Arimo:wght@400&display=swap">
<style>
  :root {
    --green: #4cae45;
    --green-dark: #3f9a39;
    --green-text: #3aa23a;
    --ink: #333333;
    --muted: #666666;
    --line: #d6d6d6;
    --panel: #f7f7f7;
    --icon-bg: #dcdcdc;
    --dark: #2e2e2e;
    --white: #ffffff;
  }
  * { box-sizing: border-box; margin: 0; padding: 0; }
  html, body { width: 834px; height: 1200px; overflow: hidden; background: var(--white); }
  body { position: relative; font-family: "Ubuntu", sans-serif; color: var(--ink); }
  .abs { position: absolute; }

  .top-bar { left: 0; top: 0; width: 834px; height: 32px; border-top: 3px solid var(--green); border-bottom: 1px solid var(--line); }
  .top-bar__note { left: 14px; top: 11px; font-family: "Arimo", sans-serif; font-size: 9.6px; color: #888; }
  .top-bar__note a { color: var(--green-text); text-decoration: none; }
  .social { right: 22px; top: 7px; display: flex; gap: 5px; }
  .social span { width: 18px; height: 18px; background: #e4e4e4; display: block; }

  .header { left: 0; top: 32px; width: 834px; height: 84px; background: linear-gradient(#fafafa, #ffffff); }
  .brand { left: 14px; top: 48px; display: flex; align-items: center; gap: 8px; }
  .brand__dot { width: 30px; height: 30px; border-radius: 50%; background: var(--green); }
  .brand__name { font-size: 40px; font-weight: 500; color: #4a4a4a; letter-spacing: -1px; }
  .search { left: 640px; top: 66px; width: 170px; height: 21px; border: 1px solid var(--line); border-radius: 11px; font-size: 8.5px; color: #888; padding: 5px 12px; }
  .search svg { position: absolute; right: 8px; top: 4px; }

  .nav { left: 14px; top: 147px; display: flex; gap: 21px; font-family: "Arimo", sans-serif; font-size: 14px; color: #444; }
  .nav a { color: inherit; text-decoration: none; line-height: 19px; }
  .nav .is-active { background: var(--green); color: var(--white); padding: 0 5px; }
  .login { left: 696px; top: 147px; display: flex; align-items: center; gap: 4px; }
  .login__btn { background: var(--green); color: var(--white); font-family: "Arimo", sans-serif; font-size: 13.5px; padding: 2px 5px; }

  .hero { left: 0; top: 187px; width: 834px; height: 379px; background: radial-gradient(ellipse at 50% 35%, #8a8a8a 0%, #4c4c4c 55%, #2a2a2a 100%); }
  .hero__cap { left: 13px; background: rgba(0,0,0,.75); color: var(--white); }
  .hero__title { top: 472px; background: var(--green); font-size: 22px; padding: 2px 6px; }
  .hero__line1 { top: 506px; font-size: 15.5px; padding: 1px 6px 1px 9px; }
  .hero__line2 { top: 531px; font-size: 18px; padding: 1px 6px; background: rgba(60,60,60,.75); }

  .intro__title { left: 0; width: 834px; top: 618px; text-align: center; font-size: 24px; color: var(--green-text); }
  .intro__text { left: 13px; width: 808px; font-size: 8.8px; line-height: 12.4px; color: #444; }
  .rule { left: 14px; top: 786px; width: 800px; height: 1px; background: #555; }
  .more { left: 700px; top: 768px; width: 114px; height: 19px; background: var(--dark); color: var(--white); font-size: 10px; display: flex; align-items: center; gap: 5px; padding-left: 4px; }

  .feature { width: 390px; height: 78px; border: 1px solid var(--line); background: var(--panel); }
  .feature__title { position: absolute; left: 8px; top: 6px; font-size: 16px; color: var(--green-text); }
  .feature__text { position: absolute; left: 8px; top: 31px; font-size: 11.5px; color: var(--muted); }
  .feature__text.is-dark { color: var(--ink); }
  .feature__icon { position: absolute; right: 0; top: 0; width: 77px; height: 76px; background: var(--icon-bg); }
  .feature__icon.is-green { background: var(--green); display: flex; align-items: center; justify-content: center; }

  .footer { left: 0; top: 1042px; width: 834px; height: 152px; background: var(--green); color: var(--white); }
  .footer__bar { left: 0; top: 1194px; width: 834px; height: 6px; background: var(--dark); }
  .footer h3 { position: absolute; top: 1049px; font-weight: 400; font-size: 16px; }
  .footer__rule { left: 185px; top: 1069px; width: 629px; height: 1px; background: rgba(255,255,255,.7); }
  .footer__divider { top: 1084px; width: 1px; height: 108px; background: rgba(255,255,255,.45); }
  .links { left: 20px; top: 1079px; list-style: none; font-size: 10.4px; }
  .links li { height: 19.2px; line-height: 19.2px; display: flex; align-items: center; gap: 8px; }
  .quote { left: 183px; top: 1082px; width: 316px; height: 104px; background: var(--green-dark); font-size: 10.4px; line-height: 14.4px; padding: 10px 12px 0 23px; }
  .quote__author { position: absolute; right: 5px; bottom: 6px; font-size: 10.4px; color: #234; }
  .helpline__num { left: 543px; top: 1090px; font-size: 25px; font-weight: 500; }
  .helpline__text { left: 545px; top: 1128px; font-size: 10.4px; line-height: 19px; }
</style>
</head>
<body>

<div class="abs top-bar"></div>
<p class="abs top-bar__note">If you like Our Services you can contact Us at +61 (0) 3 5550 0142 or by sending Us an email at <a>&#9993; hello@quilanorte.com</a></p>
<div class="abs social"><span></span><span></span><span></span><span></span><span></span></div>

<div class="abs header"></div>
<div class="abs brand"><span class="brand__dot"></span><span class="brand__name">quilanorte</span></div>
<div class="abs search">Search
  <svg width="11" height="11" viewBox="0 0 11 11"><circle cx="4.5" cy="4.5" r="3.3" fill="none" stroke="#aaa" stroke-width="1.3"/><line x1="7" y1="7" x2="10" y2="10" stroke="#aaa" stroke-width="1.5"/></svg>
</div>

<nav class="abs nav">
  <a class="is-active">HOME</a><a>WHY QUILANORTE</a><a>PRODUCTS</a><a>SERVICES</a><a>RESELLER</a><a>CONTACT</a>
</nav>
<div class="abs login">
  <svg width="18" height="22" viewBox="0 0 18 22"><circle cx="9" cy="6" r="4.5" fill="#777"/><path d="M1 20c0-5 3.5-8 8-8s8 3 8 8z" fill="#777"/></svg>
  <span class="login__btn">USER LOGIN</span>
</div>

<div class="abs hero" role="img" aria-label="Team of business people in suits standing with arms crossed over a faint world map"></div>
<div class="abs hero__cap hero__title">LOCAL PRESENCE</div>
<div class="abs hero__cap hero__line1">Everywhere you can count on us.</div>
<div class="abs hero__cap hero__line2">The best solution for your business</div>

<h1 class="abs intro__title" style="font-weight:400">GIVE YOUR CUSTOMERS A CHOICE OF 250 TOP LEVEL DOMAINS (TLDS)</h1>
<p class="abs intro__text" style="top:657px">Quilanorte is mainly focused the the latin american marked. Today Quilanorte is the fastest growing .br registrar and today many of the world’s largest registrars are using Quilanortenic to register .br domain with or without local present. With the unique QuilanorteNIC registration engine, you can offer your customers more than 200 top-level domains (TLDs).</p>
<p class="abs intro__text" style="top:695px">It is ideal for companies wishing to go beyond the usual narrow range of TLDs and differentiate themselves from competitors by offering a much larger portfolio. Your customers can register domains worldwide through one user-friendly interface. It is easily integrated into your existing order provisioning system, using our XML API, Quilanorte Web Service, or standard email templates. You can also submit orders directly through the Quilanorte web interface. Our local presence services mean you can offer your customers everything they are likely to want – including restricted TLDs in countries where a presence on the ground is required.</p>

<div class="abs rule"></div>
<div class="abs more">
  <svg width="16" height="10" viewBox="0 0 16 10"><path d="M1 1l4 4-4 4M8 1l4 4-4 4" fill="none" stroke="#fff" stroke-width="2"/></svg>
  Continue Reading
</div>

<div class="abs feature" style="left:10px;top:823px">
  <h2 class="feature__title" style="font-weight:400">Security</h2>
  <p class="feature__text is-dark">Protecting &nbsp;your brand against undesire association</p>
  <div class="feature__icon is-green">
    <svg width="44" height="44" viewBox="0 0 44 44"><circle cx="22" cy="22" r="19" fill="#fff"/><path d="M12 22l7 7 13-14" fill="none" stroke="var(--green)" stroke-width="5"/></svg>
  </div>
</div>
<div class="abs feature" style="left:427px;top:823px">
  <h2 class="feature__title" style="font-weight:400">TLD Expecilist</h2>
  <p class="feature__text">Providing a large potfolio for your clients</p>
  <div class="feature__icon" role="img" aria-label="Grey puzzle pieces illustration"></div>
</div>
<div class="abs feature" style="left:10px;top:929px">
  <h2 class="feature__title" style="font-weight:400">Automation</h2>
  <p class="feature__text">Domain process quick and reliable</p>
  <div class="feature__icon" role="img" aria-label="Metallic gear illustration"></div>
</div>
<div class="abs feature" style="left:427px;top:929px">
  <h2 class="feature__title" style="font-weight:400">Personal Service</h2>
  <p class="feature__text" style="top:27px">High qualified professionals at your service</p>
  <div class="feature__icon" role="img" aria-label="Silver service disc illustration"></div>
</div>

<footer class="abs footer"></footer>
<h3 class="footer__col" style="position:absolute;left:24px;top:1049px;font-weight:400;font-size:16px;color:#fff">Main Links</h3>
<h3 style="position:absolute;left:185px;top:1049px;font-weight:400;font-size:16px;color:#fff">Client Testimonials</h3>
<h3 style="position:absolute;left:538px;top:1049px;font-weight:400;font-size:16px;color:#fff">Quick Helpline</h3>
<div class="abs footer__rule"></div>
<div class="abs footer__divider" style="left:142px"></div>
<div class="abs footer__divider" style="left:526px"></div>
<ul class="abs links" style="color:#fff">
  <li><svg width="6" height="8" viewBox="0 0 6 8"><path d="M1 1l3 3-3 3" fill="none" stroke="#fff" stroke-width="1.6"/></svg>HOME</li>
  <li><svg width="6" height="8" viewBox="0 0 6 8"><path d="M1 1l3 3-3 3" fill="none" stroke="#fff" stroke-width="1.6"/></svg>WHY QUILANORTE</li>
  <li><svg width="6" height="8" viewBox="0 0 6 8"><path d="M1 1l3 3-3 3" fill="none" stroke="#fff" stroke-width="1.6"/></svg>PRODUCTS</li>
  <li><svg width="6" height="8" viewBox="0 0 6 8"><path d="M1 1l3 3-3 3" fill="none" stroke="#fff" stroke-width="1.6"/></svg>SERVICES</li>
  <li><svg width="6" height="8" viewBox="0 0 6 8"><path d="M1 1l3 3-3 3" fill="none" stroke="#fff" stroke-width="1.6"/></svg>RESELLER</li>
  <li><svg width="6" height="8" viewBox="0 0 6 8"><path d="M1 1l3 3-3 3" fill="none" stroke="#fff" stroke-width="1.6"/></svg>CONTACT</li>
</ul>
<blockquote class="abs quote" style="color:#fff">
  Lorem Ipsum is simply dummy text of the printing and typesetting industry. Lorem Ipsum has been the industry's standard dummy text ever since the 1500s, when an unknown printer.
  <cite class="quote__author" style="font-style:normal">Dana Morel ( Brightfield Co)</cite>
</blockquote>
<p class="abs helpline__num" style="color:#fff">+61 (0) 3 5550 0142</p>
<p class="abs helpline__text" style="color:#fff">Contact Us Any Time 24/7<br>We are always ready to assist you</p>
<div class="abs footer__bar"></div>

</body>
</html>
```